Pedal Wardens stationary
business card, letter head, powerpoint template
Creative Brief
Use same font as used in my logo
Tomas Lindqvo
Owner & Managing Director
Ekbackevägen 14 17452 Sundbyö
tomas@pedalwardens.cc
www.pedalwardens.cc
org.nr. 558213-4406
Business card and stationary design. We provide umpires & referees for teams/organizations.

```html
<!DOCTYPE html>
<html lang="en">
<head>
<meta charset="utf-8">
<title>Pedal Wardens — Business Card</title>
<link href="https://fonts.googleapis.com/css2?family=Josefin+Sans:wght@300&family=Open+Sans:wght@400;600&display=swap" rel="stylesheet">
<style>
  :root {
    --backdrop: #e4e2df;
    --card-white: #ffffff;
    --card-dark: #3b3b3d;
    --card-band: #545456;
    --ink-dark: #2e2e30;
    --ink-light: #f2f2f2;
    --ink-muted: #c9c9cb;
  }
  html, body {
    margin: 0;
    width: 1200px;
    height: 902px;
    overflow: hidden;
    background: var(--backdrop);
  }
  .card {
    position: absolute;
    left: 100px;
    top: 165px;
    width: 1000px;
    height: 572px;
    background: var(--card-dark);
    box-shadow: 0 10px 30px rgba(0,0,0,0.25);
    overflow: hidden;
    font-family: "Open Sans", Arial, sans-serif;
  }
  .card-shapes {
    position: absolute;
    inset: 0;
  }
  .brand {
    position: absolute;
    left: 46px;
    top: 62px;
    display: flex;
    align-items: center;
    gap: 22px;
  }
  .brand-dot {
    width: 82px;
    height: 82px;
    border-radius: 50%;
    background: var(--ink-dark);
  }
  .brand-name {
    font-family: "Josefin Sans", Arial, sans-serif;
    font-weight: 300;
    font-size: 52px;
    letter-spacing: 7px;
    color: var(--ink-dark);
    text-transform: uppercase;
    padding-top: 8px;
  }
  .person {
    position: absolute;
    right: 46px;
    top: 262px;
    text-align: right;
    color: var(--ink-light);
  }
  .person-name {
    font-weight: 600;
    font-size: 27px;
    margin: 0 0 6px;
  }
  .person-title {
    font-size: 21px;
    margin: 0;
  }
  .contact {
    position: absolute;
    left: 40px;
    top: 342px;
    margin: 0;
    padding: 0;
    list-style: none;
    color: var(--ink-light);
    font-size: 22px;
  }
  .contact li {
    display: flex;
    align-items: center;
    gap: 12px;
    height: 40px;
  }
  .contact svg {
    width: 28px;
    height: 28px;
    flex: none;
  }
  .band-url {
    position: absolute;
    right: 46px;
    top: 449px;
    color: var(--ink-muted);
    font-size: 17px;
    letter-spacing: 5px;
  }
</style>
</head>
<body>
  <div class="card">
    <svg class="card-shapes" viewBox="0 0 1000 572" width="1000" height="572" aria-hidden="true">
      <rect x="0" y="0" width="1000" height="222" fill="var(--card-white)"/>
      <polygon points="784,222 816,222 800,240" fill="var(--card-white)"/>
      <path d="M460,486 C540,486 560,420 640,420 L1000,420 L1000,486 Z" fill="var(--card-band)"/>
    </svg>

    <div class="brand">
      <div class="brand-dot"></div>
      <div class="brand-name">Pedal Wardens</div>
    </div>

    <div class="person">
      <p class="person-name">Tomas Lindqvo</p>
      <p class="person-title">Owner &amp; Managing Director</p>
    </div>

    <ul class="contact">
      <li>
        <svg viewBox="0 0 28 28" aria-hidden="true">
          <circle cx="14" cy="14" r="14" fill="var(--ink-light)"/>
          <path d="M7 14 L14 8 L21 14 M9 13 V20 H19 V13" fill="none" stroke="var(--card-dark)" stroke-width="2"/>
        </svg>
        Ekbackevägen 14 17452 Sundbyö
      </li>
      <li>
        <svg viewBox="0 0 28 28" aria-hidden="true">
          <circle cx="14" cy="14" r="14" fill="var(--ink-light)"/>
          <rect x="7.5" y="9.5" width="13" height="9" fill="none" stroke="var(--card-dark)" stroke-width="1.8"/>
          <path d="M7.5 9.5 L14 15 L20.5 9.5" fill="none" stroke="var(--card-dark)" stroke-width="1.8"/>
        </svg>
        tomas@pedalwardens.cc
      </li>
      <li>
        <svg viewBox="0 0 28 28" aria-hidden="true">
          <circle cx="14" cy="14" r="14" fill="var(--ink-light)"/>
          <circle cx="14" cy="14" r="7" fill="none" stroke="var(--card-dark)" stroke-width="1.6"/>
          <ellipse cx="14" cy="14" rx="3" ry="7" fill="none" stroke="var(--card-dark)" stroke-width="1.4"/>
          <path d="M7 14 H21" stroke="var(--card-dark)" stroke-width="1.4"/>
        </svg>
        www.pedalwardens.cc
      </li>
    </ul>

    <div class="band-url">www.PedalWardens.cc</div>
  </div>
</body>
</html>
```